Web Design Project

This web site is to be designed for a popular Cambodian singer, Kesa Morinth. Web site name "Kesa Morinth".

The purpose is to keep her fans update with the latest of her entertainment career and invite them to help raising fund for Mekong Little Hands Fund.

In addition to other normal pages such as HOME, ABOUT... This web site must be:
1. able to link to Dropshipers and add Products
2. able to donate (accept Major Credit Cards or CoinLark)
3. able to purchase products (accept Major Credit Cards or CoinLark)
4. able to video live chat with Kesa Morinth
5. able to book appointment on her calendar

Here is a sample of the web site:
http://dorvel22.sitebarn.example/pich-lea-kena

Please call me if you need any clarification at 1-555-284-1937 or leave your number for me to call you back.

Thank you

Vuthy

Target Market(s)

Cambodian living abroad

Industry/Entity Type

Entertainment

Requirements
Must have
• 1. able to link to Dropshipers and add Products
2. able to Donate (accept Major Credit Cards or CoinLark)

```html
<!DOCTYPE html>
<html lang="en">
<head>
<meta charset="utf-8">
<title>Kesa Morinth</title>
<link href="https://fonts.googleapis.com/css2?family=Source+Sans+3:wght@400;600&family=Arimo:wght@400;700&display=swap" rel="stylesheet">
<style>
:root{
  --blue:#2a6bb8;
  --blue-dark:#1f5caa;
  --blue-light:#3a86d6;
  --ink:#222;
  --grey-text:#666;
  --header-bg:#eef0f2;
  --line:#c9ced4;
  --white:#fff;
}
*{box-sizing:border-box;margin:0;padding:0}
html,body{width:1163px;height:1200px;overflow:hidden;background:var(--white)}
body{font-family:"Source Sans 3",sans-serif;color:var(--ink)}
.page{position:relative;width:1200px;height:1238px;transform:scale(.96917);transform-origin:0 0}
.abs{position:absolute}

.site-header{left:0;top:0;width:1200px;height:138px;background:var(--header-bg)}
.account-bar{left:595px;top:0;width:490px;height:32px;background:linear-gradient(#3b86d4,#1f60ad);clip-path:polygon(0 0,100% 0,96% 100%,4% 100%);display:flex;justify-content:center;align-items:center;gap:12px;color:var(--white);font-size:13px;font-weight:600}
.logo{left:128px;top:30px;font-size:42px;color:var(--blue);letter-spacing:.5px}
.follow{left:838px;top:61px;font-size:12px;font-weight:600;text-transform:uppercase}
.socials{left:930px;top:60px;display:flex;gap:10px;font-size:12px;color:var(--blue-dark);font-weight:600}
.socials span{display:flex;align-items:center;gap:4px}
.socials i{width:11px;height:11px;border-radius:50%;background:var(--blue);display:inline-block}
.main-nav{left:458px;top:86px;display:flex;align-items:center;font-size:18px}
.main-nav a{color:var(--ink);text-decoration:none;margin-right:27px}
.main-nav a.active{background:linear-gradient(#3d8ad8,#2160ae);color:var(--white);padding:6px 19px;border-radius:6px;margin-right:25px}

.hero-band{left:0;top:138px;width:1200px;height:386px;background:linear-gradient(#2f78c8,#1f5fae)}
.hero{left:102px;top:151px;width:994px;height:452px;background:var(--white);border-radius:8px;box-shadow:0 10px 16px -8px rgba(0,0,0,.35);overflow:hidden}
.hero-photo{left:0;top:0;width:640px;height:452px;background:linear-gradient(90deg,#d8c9ae 0%,#c9b694 45%,#e6dcc8 80%,#ffffff 100%)}
.hero-title{left:584px;top:58px;font-size:52px;color:var(--blue);white-space:nowrap;font-weight:400}
.hero-text{left:585px;top:126px;width:345px;font-size:20px;line-height:24px}
.btn{display:flex;align-items:center;justify-content:center;color:var(--white);font-size:21px;border-radius:5px}
.btn-quote{left:586px;top:280px;width:165px;height:34px;background:linear-gradient(#4b95de,#1f60ad)}
.btn-donate{left:767px;top:280px;width:165px;height:34px;background:linear-gradient(#555,#222)}
.slider-dots{left:881px;top:387px;display:flex;gap:9px}
.slider-dots i{width:12px;height:12px;border-radius:50%;background:#333;display:block}
.slider-dots i.on{background:var(--blue-light)}

.section-title{font-size:25px;color:var(--blue);font-weight:400}
.welcome-text{left:111px;top:666px;width:641px;font-size:12.4px;line-height:18px;text-align:justify}
.video{left:771px;top:646px;width:308px;height:175px;background:#111}
.video-frame{left:0;top:0;width:308px;height:156px;background:linear-gradient(90deg,#2a2420,#5b4a3f 40%,#3a2e27 70%,#6a5648)}
.video-play{left:133px;top:64px;width:38px;height:26px;background:rgba(0,0,0,.75);border-radius:5px}
.video-bar{left:0;top:156px;width:308px;height:19px;background:#161616;color:#aaa;font-size:6px}
.video-progress{left:0;top:157px;width:308px;height:3px;background:#555}
.video-progress b{display:block;width:72px;height:3px;background:#d22}

.divider{top:820px;width:1px;height:350px;background:linear-gradient(transparent,#dde1e5 30%,#dde1e5 70%,transparent)}
.post{left:112px;width:270px;height:86px;border-bottom:1px dotted #ccc}
.post-thumb{left:0;top:0;width:95px;height:66px;border:3px solid var(--white);box-shadow:0 1px 3px rgba(0,0,0,.4)}
.post-title{left:104px;top:0;font-family:Arimo,sans-serif;font-size:14.5px}
.post-text{left:107px;top:20px;width:160px;font-family:Arimo,sans-serif;font-size:12px;line-height:18px;color:var(--grey-text)}

.form-label{width:70px;text-align:right;font-family:Arimo,sans-serif;font-size:14px;left:406px}
.field{left:488px;width:197px;height:34px;border:1px solid var(--line);border-radius:8px;font-family:Arimo,sans-serif;font-size:12px;color:#666;padding:10px 14px;background:var(--white)}
.btn-book{left:478px;top:1105px;width:179px;height:37px;background:linear-gradient(#555,#1e1e1e);border-radius:4px;font-size:15px;font-weight:600;color:var(--white);display:flex;align-items:center;justify-content:center;box-shadow:0 4px 4px -2px rgba(0,0,0,.3)}

.chat{left:766px;top:893px;width:309px;height:257px;border:1px solid #b9bec4;background:#f5f5f5;font-family:Arimo,sans-serif}
.chat-head{left:0;top:0;width:307px;height:36px;background:linear-gradient(#d4d4d4,#9d9d9d);color:var(--white);font-size:13px;font-weight:700;padding:11px 0 0 42px}
.chat-bubble{left:14px;top:10px;width:20px;height:14px;background:#7cc33a;border-radius:50%}
.chat-ctrl{top:9px;width:18px;height:18px;border-radius:50%;background:#eee;border:1px solid #999}
.chat-welcome{left:14px;top:42px;font-size:12px;color:#555;line-height:14px}
.chat-log{left:12px;top:89px;width:287px;height:89px;border:1px solid var(--line);background:var(--white);font-size:11px;line-height:13px;padding:8px;color:#333}
.chat-log .who-a{color:var(--blue)}
.chat-log .who-b{color:#d33}
.chat-input{left:12px;top:183px;width:287px;height:30px;border:1px solid var(--line);border-radius:3px;background:var(--white);font-size:11px;color:#888;padding:8px 10px}
.chat-send{left:14px;top:219px;width:70px;height:29px;background:linear-gradient(#bbb,#777);border:1px solid #666;color:var(--white);font-weight:700;font-size:13px;display:flex;align-items:center;justify-content:center}
.chat-phone{left:126px;top:227px;font-size:12px;color:#555;font-weight:700;display:flex;gap:5px;align-items:center}

.site-footer{left:0;top:1190px;width:1200px;height:48px;background:linear-gradient(#3a83d1,#1f5fae)}
.payments{left:107px;top:16px;display:flex;gap:16px;color:var(--white);font-size:12px;font-weight:600}
.payments span{display:flex;align-items:center;gap:4px}
.payments i{width:9px;height:9px;background:var(--white);display:inline-block}
.copyright{left:912px;top:16px;color:var(--white);font-size:13px}
</style>
</head>
<body>
<div class="page">

  <header class="site-header abs">
    <nav class="account-bar abs">
      <span>MY ACCOUNT</span><span>|</span>
      <span>MY CART</span><span>|</span>
      <span>SIGN IN</span><span>|</span>
      <span>CHECK OUT</span>
    </nav>
    <div class="logo abs">Kesa Morinth</div>
    <div class="follow abs">Follow us on</div>
    <div class="socials abs">
      <span><i></i>Chirpa</span>
      <span><i></i>Folkbook</span>
      <span><i></i>Workmesh</span>
    </div>
    <nav class="main-nav abs">
      <a class="active" href="#">Home</a>
      <a href="#">About</a>
      <a href="#">Products</a>
      <a href="#">Feedback</a>
      <a href="#">Donate</a>
      <a href="#">Events</a>
      <a href="#">Contact Us</a>
    </nav>
  </header>

  <div class="hero-band abs"></div>
  <section class="hero abs">
    <div class="hero-photo abs" role="img" aria-label="Portrait photo of the singer beside a window shutter"></div>
    <h1 class="hero-title abs">Kesa Morinth</h1>
    <p class="hero-text abs">Contrary to popular belief, Lorem Ipsum is not simply random text. It has roots in a piece of classical Latin literature from 45 BC, making it over 2000 years old. Edwin Harlow,</p>
    <div class="btn btn-quote abs">Get a Quote</div>
    <div class="btn btn-donate abs">Donate Now!</div>
    <div class="slider-dots abs"><i class="on"></i><i></i><i></i><i></i></div>
  </section>

  <h2 class="section-title abs" style="left:108px;top:626px">Welcome to Our Website</h2>
  <p class="welcome-text abs">Contrary to popular belief, Lorem Ipsum is not simply random text. It has roots in a piece of classical Latin literature from 45 BC, making it over 2000 years old. Edwin Harlow, a Latin professor at Ashford Hill College in Vermont But I must explain to you how all this mistaken idea of denouncing pleasure and praising pain was born and I will give you a complete account of the system, and expound the actual teachings of the great explorer of the truth, the master-builder of human happiness. No one rejects, dislikes, or avoids pleasure itself, because it is pleasure, but because those who do not know how to pursue pleasure rationally encounter consequences that are extremely painful. Nor again is there anyone who loves or pursues or desires to obtain pain of itself, because it is pain, but because occasionally circumstances occur in which toil and pain can procure him some...</p>

  <div class="video abs">
    <div class="video-frame abs" role="img" aria-label="Video still of the singer with a friend"></div>
    <div class="video-play abs">
      <svg width="38" height="26" viewBox="0 0 38 26"><polygon points="15,7 25,13 15,19" fill="#fff"/></svg>
    </div>
    <div class="video-progress abs"><b></b></div>
    <div class="video-bar abs">
      <span class="abs" style="left:46px;top:8px">0:02 / 0:10</span>
      <span class="abs" style="left:262px;top:8px">720p</span>
    </div>
  </div>

  <div class="divider abs" style="left:395px"></div>
  <div class="divider abs" style="left:735px"></div>

  <h2 class="section-title abs" style="left:111px;top:852px">Events</h2>
  <article class="post abs" style="top:897px">
    <div class="post-thumb abs" role="img" aria-label="Event photo of a smiling woman" style="background:linear-gradient(135deg,#b33a3a,#d9b59a)"></div>
    <div class="post-title abs">This is a sample Post 1</div>
    <div class="post-text abs">Lorem ipsum dolor sit amet, consectetuer adipiscing elit, sed diam nonummy nibh...</div>
  </article>
  <article class="post abs" style="top:987px">
    <div class="post-thumb abs" role="img" aria-label="Event photo of a man holding a bottle in a shop" style="background:linear-gradient(135deg,#c79a3b,#e8dcc2)"></div>
    <div class="post-title abs">This is a sample Post 1</div>
    <div class="post-text abs">Lorem ipsum dolor sit amet, consectetuer adipiscing elit, sed diam nonummy nibh...</div>
  </article>
  <article class="post abs" style="top:1077px">
    <div class="post-thumb abs" role="img" aria-label="Event photo of a woman in a blue top" style="background:linear-gradient(135deg,#b33a3a,#9fb3cc)"></div>
    <div class="post-title abs">This is a sample Post 1</div>
    <div class="post-text abs">Lorem ipsum dolor sit amet, consectetuer adipiscing elit, sed diam nonummy nibh...</div>
  </article>

  <h2 class="section-title abs" style="left:443px;top:852px">Book Appointment</h2>
  <form class="booking">
    <label class="form-label abs" style="top:901px">Name</label>
    <div class="field abs" style="top:895px">Enter your name</div>
    <label class="form-label abs" style="top:945px">Date</label>
    <div class="field abs" style="top:937px">mm / dd / yy</div>
    <label class="form-label abs" style="top:989px">Time</label>
    <div class="field abs" style="top:980px">00 : 00 : 00 : 00</div>
    <label class="form-label abs" style="top:1033px">Message</label>
    <div class="field abs" style="top:1024px;height:69px"></div>
    <div class="btn-book abs">Book an Appointment</div>
  </form>

  <h2 class="section-title abs" style="left:765px;top:852px">Video / Live chat</h2>
  <aside class="chat abs">
    <div class="chat-head abs">Live Chat Online
      <span class="chat-bubble abs"></span>
      <span class="chat-ctrl abs" style="left:183px"><svg width="16" height="16" viewBox="0 0 16 16"><rect x="4" y="7" width="8" height="2" fill="#777"/></svg></span>
      <span class="chat-ctrl abs" style="left:206px"><svg width="16" height="16" viewBox="0 0 16 16"><path d="M5 5 L11 11 M11 5 L5 11" stroke="#777" stroke-width="1.6"/></svg></span>
    </div>
    <p class="chat-welcome abs">Welcome! You are chatting with<br>Sophie, Sales Executive.</p>
    <div class="chat-log abs">
      <p><span class="who-a">Sophie</span>:&nbsp; Welcome to PixelHarbor.com.<br>How may I help you?</p>
      <p style="margin-top:6px"><span class="who-b">Customer</span>:&nbsp; Do you have any plans to<br>offer premium files?</p>
      <p style="margin-top:6px;color:#aaa;font-style:italic">Sophie typing message...</p>
    </div>
    <div class="chat-input abs">Type Message</div>
    <div class="chat-send abs">SEND</div>
    <div class="chat-phone abs">
      <svg width="10" height="12" viewBox="0 0 10 12"><path d="M2 0 L4 3 L3 4.5 Q4 7.5 6 8.5 L7.5 7.5 L10 9.5 L8.5 12 Q2 10 0 2 Z" fill="#777"/></svg>
      123-456-7890
    </div>
  </aside>

  <footer class="site-footer abs">
    <div class="payments abs">
      <span><i></i>Meridian</span>
      <span><i></i>CoinLark</span>
      <span><i></i>Velto</span>
      <span><i></i>Atlas Express</span>
      <span><i></i>Discovo</span>
    </div>
    <div class="copyright abs">© 2012.www.kesamorinth.example</div>
  </footer>

</div>
</body>
</html>
```